依頼詳細
タイ古式マッサージの看板ポスターを作成依頼をお願いします。
サイズはA2サイズです。よろしくお願いします。
例文は添付致します。
記載項目
店舗名、電話番号、ロゴ
希望イメージ
シンプル 複雑
単色 カラフル
暗い 明るい
日常 高級
遊び心 厳粛
未来的 伝統的
女性的 男性的
希望する色
赤系、茶系、緑系、グレー系
納品ファイル
• 高解像度JPG (.jpg)
• イラストレーター形式 (.ai)
補足説明
スタンド看板にしますのでA2サイズでなく原稿サイズ435x940でお願いします。
すみませんがよろしくお願いします。

色がとてもいいです!! パッと見て目立つしわかりやすいと思いました。
ありがとうございました。

この度は、皆様方にご提案頂きまして誠にありがとうございました。
また、何かございましたらよろしくお願いします。
ありがとうございました。

```html
<!DOCTYPE html>
<html lang="ja">
<head>
<meta charset="utf-8">
<title>タイ古式マッサージ</title>
<link href="https://fonts.googleapis.com/css2?family=Noto+Serif+JP:wght@400;600;700;900&family=Noto+Sans+JP:wght@500;700&display=swap" rel="stylesheet">
<style>
  :root {
    --mint: #cfe3cf;
    --mint-deep: #a9c9ad;
    --ink: #3a2614;
    --brown-dark: #4a2a14;
    --brown: #7a3e16;
    --orange: #e59a48;
    --gold: #f2a446;
    --cream: #fff6e6;
    --black: #0d0906;
  }
  html, body { margin: 0; padding: 0; overflow: hidden; }
  body { width: 1200px; height: 2592px; background: var(--mint); font-family: "Noto Serif JP", serif; color: var(--ink); }
  .poster { position: relative; width: 1200px; height: 2592px; overflow: hidden;
    background: linear-gradient(180deg, #e6f1e2 0%, var(--mint) 40%, var(--mint-deep) 100%); }

  .lead { position: absolute; top: 22px; left: 0; width: 100%; text-align: center; font-weight: 700; line-height: 1.3; white-space: nowrap; }
  .lead p { margin: 0; }
  .lead .l1 { font-size: 50px; }
  .lead .l2 { font-size: 52px; }

  .title-band { position: absolute; top: 200px; left: 0; width: 100%; height: 150px; background: var(--black);
    border-top: 4px solid var(--gold); border-bottom: 4px solid var(--gold); box-sizing: border-box;
    display: flex; align-items: center; justify-content: center; }
  .title-band h1 { margin: 0; font-size: 104px; font-weight: 700; color: var(--gold); letter-spacing: 4px; }

  .intro { position: absolute; top: 392px; left: 44px; width: 790px; font-size: 33px; line-height: 1.5; margin: 0; }
  .flyer-thumb { position: absolute; top: 386px; left: 862px; width: 296px; height: 372px;
    background: linear-gradient(180deg, #3b2212, #6a3a18 55%, #2b1a0e); border: 3px solid #1e1208; }

  .glow { position: absolute; left: -160px; top: 700px; width: 1520px; height: 1420px; border-radius: 50%;
    background: radial-gradient(ellipse at center, #f0b066 0%, var(--orange) 22%, #b8621f 48%, var(--brown) 62%, rgba(122,62,22,0) 72%); }

  .lotus-mark { position: absolute; top: 790px; left: 510px; width: 180px; height: 220px; border-radius: 50% 50% 40% 40%;
    background: radial-gradient(circle, #fff3df 0%, rgba(255,243,223,0.2) 70%); }

  .voices { position: absolute; top: 1040px; left: 0; width: 100%; text-align: center; color: var(--cream); }
  .voices p { margin: 0; font-size: 60px; line-height: 1.35; font-weight: 600; }
  .invite { position: absolute; top: 1270px; left: 0; width: 100%; text-align: center; color: var(--cream); }
  .invite p { margin: 0; font-size: 54px; line-height: 1.4; font-weight: 600; }

  .prices { position: absolute; top: 1460px; left: 180px; width: 880px; color: var(--cream); }
  .price-row { display: flex; align-items: baseline; height: 160px; }
  .price-row .time { width: 380px; font-size: 92px; font-weight: 600; }
  .price-row .amount { font-size: 104px; font-weight: 600; }
  .price-row .tax { font-size: 36px; margin-left: 14px; }

  .note { position: absolute; top: 1810px; left: 0; width: 100%; text-align: center; color: var(--cream); }
  .note p { margin: 0; font-size: 34px; line-height: 1.5; }

  .phone { position: absolute; top: 2060px; left: 0; width: 100%; display: flex; justify-content: center; align-items: center; gap: 18px; }
  .phone span { font-size: 128px; font-weight: 700; font-style: italic; color: var(--ink); letter-spacing: 2px; }
  .hours { position: absolute; top: 2235px; left: 0; width: 100%; text-align: center; font-family: "Noto Sans JP", sans-serif; font-size: 42px; font-weight: 700; color: var(--ink); }
  .hours .label { background: var(--brown-dark); color: var(--cream); padding: 0 8px; margin-right: 10px; }

  .footer { position: absolute; top: 2350px; left: 0; width: 100%; height: 242px; background: var(--brown-dark);
    display: flex; align-items: center; justify-content: center; gap: 24px; }
  .footer .dot { width: 22px; height: 22px; border-radius: 50%; background: var(--cream); }
  .footer .name { font-size: 84px; font-weight: 600; letter-spacing: 8px; color: var(--cream); line-height: 1; }
</style>
</head>
<body>
<div class="poster">
  <header class="lead">
    <p class="l1">デスクワークが多く</p>
    <p class="l2">つらい首こりや肩こり、体の疲れがひどい貴方へ</p>
  </header>

  <div class="title-band"><h1>タイ古式マッサージ</h1></div>

  <p class="intro">別名「二人で行うヨガ」と言われ、もみ、押すだけでなくストレッチ施術で血行が促進し最高の柔軟性を高めていきます。なんだかプロレス技を掛けられているようなストレッチですがゆっくりと体がほぐされていくので痛くなく「世界で一番気持ちいいマッサージ」と言われています。</p>
  <div class="flyer-thumb" role="img" aria-label="タイ古式マッサージのチラシ見本"></div>

  <div class="glow"></div>
  <div class="lotus-mark" role="img" aria-label="瞑想する人のシルエットの装飾マーク"></div>

  <div class="voices">
    <p>「気づいたら、寝ていた」</p>
    <p>「ビックリするほど体が軽くなった」</p>
  </div>
  <div class="invite">
    <p>などのお声をいただく</p>
    <p>タイ古式マッサージを体験してみませんか？</p>
  </div>

  <div class="prices">
    <div class="price-row"><span class="time">30 分</span><span class="amount">￥3,500</span><span class="tax">(税込)</span></div>
    <div class="price-row"><span class="time">60 分</span><span class="amount">￥5,900</span><span class="tax">(税込)</span></div>
  </div>

  <div class="note">
    <p>全身をほぐしますので</p>
    <p>クイックマッサージにはない効果が実感できます</p>
  </div>

  <div class="phone">
    <svg width="90" height="110" viewBox="0 0 24 30" aria-hidden="true">
      <path d="M6 2 C3 3 2 6 3 10 C5 18 10 25 16 28 C19 29 21 27 22 25 L18 20 C17 19 16 19 15 20 L13 21 C10 18 8 14 7 11 L9 9 C10 8 10 7 9 6 Z" fill="#3a2614"/>
    </svg>
    <span>03-4170-2286</span>
  </div>
  <div class="hours"><span class="label">【受付時間】</span>10：00～21：00（20：30最終）</div>

  <footer class="footer">
    <span class="dot"></span>
    <span class="name">SORANE</span>
  </footer>
</div>
</body>
</html>
```